Business Card Design for a Lending Business (Hard Money loans)

We need a business card for our Real Estate Lending business. We do hard Money loans for real estate investors. We have an existing logo we like, see attached. I'd like the business card to mostly include the logo colors, but a bright color pop of some sort would be nice to see also. Card should include Logo, Company Name, Company Address, Employee Name, Cell Phone, Main Phone, Email, Website

Industry/Entity Type

Finance / Lending

Contact Information for Business Card

Logo, Company Name, Company Address, Employee Name, Cell Phone, Main Phone, Email, Website

Requirements
Nice to have
• I'd like the business card to mostly include the logo colors, but a bright color pop of some sort would be nice to see also.

```html
<!DOCTYPE html>
<html lang="en">
<head>
<meta charset="utf-8">
<title>Crestline Lending – Business Card</title>
<link rel="stylesheet" href="https://fonts.googleapis.com/css2?family=Montserrat:wght@400;500;600;700&display=swap">
<style>
  :root {
    --backdrop: #2b2b2b;
    --brand-blue: #03268a;
    --brand-cyan: #00a9e2;
    --paper: #ffffff;
    --ink: #222a36;
  }
  * { box-sizing: border-box; margin: 0; padding: 0; }
  html, body { width: 1200px; height: 875px; overflow: hidden; }
  body {
    background: var(--backdrop);
    font-family: "Montserrat", Arial, sans-serif;
    position: relative;
  }
  .card {
    position: absolute;
    width: 520px;
    height: 298px;
    border-radius: 18px;
    overflow: hidden;
  }

  /* Front */
  .card-front {
    left: 70px; top: 130px;
    background: var(--brand-blue);
    display: flex; flex-direction: column; align-items: center; justify-content: center;
  }
  .front-wordmark {
    color: var(--paper);
    font-weight: 700;
    font-size: 38px;
    letter-spacing: 3px;
    text-align: center;
    line-height: 1.15;
  }
  .front-wordmark .sub { display: block; font-size: 17px; letter-spacing: 10px; }
  .front-rule {
    margin-top: 14px;
    width: 300px; height: 2px;
    background: var(--brand-cyan);
  }

  /* Back */
  .card-back {
    left: 610px; top: 440px;
    background: var(--paper);
  }
  .name-band {
    position: absolute;
    left: 150px; right: 0; top: 38px; height: 92px;
    background: var(--brand-blue);
    display: flex; flex-direction: column; align-items: flex-end; justify-content: center;
    padding-right: 30px;
  }
  .person-name { color: var(--paper); font-weight: 600; font-size: 26px; letter-spacing: 1px; }
  .person-title { color: var(--brand-cyan); font-size: 14px; font-weight: 500; margin-top: 2px; }
  .back-wordmark {
    position: absolute; left: 26px; top: 66px;
    color: var(--brand-blue); font-weight: 700; font-size: 15px; line-height: 1.2;
    letter-spacing: 1px;
  }
  .company-block {
    position: absolute; left: 30px; bottom: 30px;
    font-size: 12px; line-height: 1.55; color: var(--ink);
  }
  .company-name { color: var(--brand-cyan); font-weight: 600; }
  .contact-list {
    position: absolute; right: 28px; bottom: 34px;
    list-style: none; font-size: 12.5px; line-height: 1.65; color: var(--ink);
    text-align: right;
  }
  .contact-list li { display: flex; align-items: center; justify-content: flex-end; gap: 8px; }
  .contact-list svg { width: 11px; height: 11px; fill: var(--brand-cyan); }
</style>
</head>
<body>

<section class="card card-front" aria-label="Card front">
  <div class="front-wordmark">CRESTLINE<span class="sub">LENDING</span></div>
  <div class="front-rule"></div>
</section>

<section class="card card-back" aria-label="Card back">
  <div class="back-wordmark">CRESTLINE<br>LENDING</div>
  <div class="name-band">
    <div class="person-name">DANIEL HART</div>
    <div class="person-title">Founder &amp; CEO</div>
  </div>

  <address class="company-block" style="font-style:normal">
    <div class="company-name">Crestline Lending Group</div>
    <div>Your Address, City, State</div>
    <div>Country, Zip Code 1235</div>
    <div>www.crestlinelending.com</div>
  </address>

  <ul class="contact-list">
    <li>(555) 210-4400
      <svg viewBox="0 0 24 24" aria-hidden="true"><path d="M6.6 10.8a15 15 0 0 0 6.6 6.6l2.2-2.2a1 1 0 0 1 1-.25 11.4 11.4 0 0 0 3.6.57 1 1 0 0 1 1 1V20a1 1 0 0 1-1 1A17 17 0 0 1 3 4a1 1 0 0 1 1-1h3.5a1 1 0 0 1 1 1c0 1.25.2 2.45.57 3.57a1 1 0 0 1-.25 1z"/></svg></li>
    <li>(555) 318-2271
      <svg viewBox="0 0 24 24" aria-hidden="true"><path d="M7 1h10a2 2 0 0 1 2 2v18a2 2 0 0 1-2 2H7a2 2 0 0 1-2-2V3a2 2 0 0 1 2-2zm0 3v15h10V4z"/></svg></li>
    <li>(555) 402-9063
      <svg viewBox="0 0 24 24" aria-hidden="true"><path d="M6 2h9l3 3v4H6zM4 10h16a2 2 0 0 1 2 2v6h-4v4H6v-4H2v-6a2 2 0 0 1 2-2zm4 7v3h8v-3z"/></svg></li>
    <li>hello@crestlinelending.com
      <svg viewBox="0 0 24 24" aria-hidden="true"><path d="M2 4h20v16H2zm2 2v.5l8 5 8-5V6z"/></svg></li>
  </ul>
</section>

</body>
</html>
```